Card Design for my dog training business Rustpaw Obedience

Need a business card design for my dog training business with my new logo. Want the card to come off professional yet fun. Want it to be very eye catchy as well. I normally have these at vet clinics, pet stores, and groomers. so need it to look better than my competitors.
Target Market(s)
dog owners
Industry/Entity Type
Dog Training
Contact Information for Business Card
needs logo, my name and info
Font styles to use
Serif
Colors
0255a3
ffffff
ec1f27
000000
333333
fbfbfb
Requirements
Must have
- Rustpaw Obedience
- Hollis Brandt
- 415 903 2267
- info@rustpawobedience.example
- www.rustpawobedience.example

```html
<!DOCTYPE html>
<html lang="en">
<head>
<meta charset="utf-8">
<title>Rustpaw Obedience — Business Card</title>
<link rel="stylesheet" href="https://fonts.googleapis.com/css2?family=EB+Garamond:ital,wght@0,500;1,400&family=Noto+Serif:wght@400&family=Quattrocento+Sans&display=swap">
<style>
  :root {
    --stage: #cbcbcb;
    --brand-blue: #0255a3;
    --blue-light: #0290dc;
    --blue-deep: #01509a;
    --paper: #fbfbfb;
    --white: #ffffff;
    --ink: #333333;
    --rule: #b5b5b5;
  }
  * { box-sizing: border-box; margin: 0; padding: 0; }
  html, body { width: 1200px; height: 992px; overflow: hidden; }
  body { background: var(--stage); position: relative; }

  .card { position: absolute; width: 357px; height: 591px; }
  .card--front {
    left: 209px; top: 202px;
    background: linear-gradient(160deg, var(--blue-light) 0%, #0170bd 35%, var(--blue-deep) 100%);
    color: var(--white);
  }
  .card--back {
    left: 634px; top: 200px;
    background: var(--paper);
    color: var(--ink);
    box-shadow: 0 0 1px rgba(0,0,0,.08);
  }

  .brand-name {
    position: absolute; left: 0; right: 0;
    text-align: center;
    font-family: "EB Garamond", serif;
    font-weight: 500;
    letter-spacing: 3px;
    text-transform: uppercase;
    line-height: 1.15;
  }
  .card--front .brand-name { top: 220px; font-size: 34px; color: var(--white); }
  .card--back .brand-name { top: 104px; font-size: 26px; color: var(--ink); }

  .tagline {
    position: absolute; left: 0; right: 0;
    text-align: center;
    font-family: "EB Garamond", serif;
    font-style: italic;
    font-size: 13.5px;
  }
  .card--front .tagline { top: 532px; color: var(--white); }
  .card--back .tagline { top: 266px; color: var(--ink); font-size: 13px; }

  .holder-name {
    position: absolute; top: 358px; left: 0; right: 0;
    text-align: center;
    font-family: "Noto Serif", serif;
    font-size: 25px;
    color: var(--brand-blue);
  }
  .holder-role {
    position: absolute; top: 398px; left: 0; right: 0;
    text-align: center;
    font-family: "Noto Serif", serif;
    font-size: 14.5px;
    color: var(--ink);
  }

  .contact-divider {
    position: absolute; top: 452px; left: 44px; right: 44px; height: 16px;
    display: flex; align-items: center; gap: 10px;
  }
  .contact-divider .rule {
    flex: 1; height: 2px;
    background: linear-gradient(90deg, transparent, var(--rule));
  }
  .contact-divider .rule--right { background: linear-gradient(90deg, var(--rule), transparent); }
  .contact-divider .icons { display: flex; gap: 10px; }

  .contact-list {
    position: absolute; top: 479px; left: 0; right: 0;
    list-style: none; text-align: center;
    font-family: "Quattrocento Sans", sans-serif;
    font-size: 15px; line-height: 21px;
    color: var(--ink);
  }
</style>
</head>
<body>
  <section class="card card--front">
    <div class="brand-name">Rustpaw<br>Obedience</div>
    <p class="tagline">“Training dogs across Texas one dog at a time.”</p>
  </section>

  <section class="card card--back">
    <div class="brand-name">Rustpaw<br>Obedience</div>
    <p class="tagline">“Training dogs across Texas one dog at a time.”</p>

    <h1 class="holder-name">Hollis Brandt</h1>
    <p class="holder-role">Dog Trainer</p>

    <div class="contact-divider">
      <span class="rule"></span>
      <span class="icons">
        <svg width="15" height="13" viewBox="0 0 15 13" aria-label="Phone">
          <path d="M1 4 Q7.5 -1 14 4 L12 6 L10 4.5 L10 3.5 Q7.5 2.5 5 3.5 L5 4.5 L3 6 Z" fill="#0255a3"/>
          <rect x="3" y="6.5" width="9" height="6" rx="1" fill="#0255a3"/>
        </svg>
        <svg width="15" height="13" viewBox="0 0 15 13" aria-label="Email">
          <rect x="0.5" y="1.5" width="14" height="10" fill="#0255a3"/>
          <path d="M0.5 1.5 L7.5 7.5 L14.5 1.5" fill="none" stroke="#fbfbfb" stroke-width="1.2"/>
        </svg>
        <svg width="14" height="14" viewBox="0 0 14 14" aria-label="Website">
          <circle cx="7" cy="7" r="6" fill="none" stroke="#0255a3" stroke-width="1.4"/>
          <ellipse cx="7" cy="7" rx="2.6" ry="6" fill="none" stroke="#0255a3" stroke-width="1.1"/>
          <path d="M1 7 H13 M2 4 H12 M2 10 H12" stroke="#0255a3" stroke-width="1.1"/>
        </svg>
      </span>
      <span class="rule rule--right"></span>
    </div>

    <ul class="contact-list">
      <li>415 903 2267</li>
      <li>info@rustpawobedience.example</li>
      <li>www.rustpawobedience.example</li>
    </ul>
  </section>
</body>
</html>
```